Mr Pellowes Yard Works flyer for newsletter

I need a professional looking flyer design for my company Mr Pellowes Yard Works based in New Braunfels, TX to boost sales. Must include the following: Lawn service starting at $40 (mowing, edging, leaf blowing) Tree trimming starting at $125. Other services-mulching, shrub trimming, aeration, flower bed maintenance, Fall/spring clean up. Serving New Braunfels and surrounding areas. To set up and estimate please call 512 555 0143 or email mrpellowesyard@example-mail.net

Industry/Entity Type

Landscaping

Font styles to use
Serif

Colors

Designer to choose colors to be used in the design.

Requirements
Must have
• Phone number 512 555 0143
• Email mrpellowesyard@example-mail.net

```html
<!DOCTYPE html>
<html lang="en">
<head>
<meta charset="utf-8">
<title>Mr Pellowes Yard Works – Flyer</title>
<link rel="stylesheet" href="https://fonts.googleapis.com/css2?family=Oswald:wght@400;500&display=swap">
<style>
  :root {
    --backdrop: #5f5e5f;
    --forest: #116b3a;
    --meadow: #e0edc3;
    --ring: #d6e7b6;
    --tangerine: #f15a24;
    --white: #ffffff;
    --grass-light: #8cc63f;
    --grass-dark: #3f8a2a;
    --mower-red: #d9262e;
  }
  * { margin: 0; padding: 0; box-sizing: border-box; }
  html, body {
    width: 917px; height: 1200px; overflow: hidden;
    background: var(--backdrop);
  }
  .canvas { position: relative; width: 917px; height: 1200px; overflow: hidden; }
  .flyer {
    position: absolute; left: 118px; top: 120px;
    width: 849px; height: 1199px;
    transform: scale(0.8); transform-origin: top left;
    font-family: "Oswald", "Arial Narrow", sans-serif;
    font-weight: 500; text-transform: uppercase;
    box-shadow: 0 4px 18px rgba(0,0,0,.35);
    overflow: hidden;
  }
  .flyer-art { position: absolute; inset: 0; }
  .brand-plate {
    position: absolute; left: 48px; top: 48px; width: 332px; height: 84px;
    background: rgba(255,255,255,.72);
    display: flex; align-items: center; justify-content: center;
  }
  .brand-name { color: var(--forest); font-size: 34px; line-height: 1; letter-spacing: .5px; }
  .offer { position: absolute; left: 45px; color: var(--white); font-size: 46px; line-height: 50px; }
  .offer .price { color: var(--tangerine); }
  .offer-lawn { top: 352px; }
  .offer-tree { top: 506px; }
  .offer-note { display: block; font-size: 20px; line-height: 28px; font-weight: 400; letter-spacing: .4px; }
  .services { position: absolute; right: 54px; top: 786px; text-align: right; }
  .services-title { color: var(--tangerine); font-size: 38px; line-height: 46px; margin-right: 2px; }
  .services-list { list-style: none; }
  .services-list li { color: var(--forest); font-size: 29px; line-height: 46px; }
  .services-list li::after {
    content: ""; display: inline-block; width: 15px; height: 15px; border-radius: 50%;
    background: var(--forest); margin-left: 11px; vertical-align: 3px;
  }
  .contact { position: absolute; left: 60px; top: 1010px; color: var(--forest); }
  .contact-lead { font-size: 38px; line-height: 44px; }
  .contact-call { display: flex; align-items: center; gap: 8px; }
  .call-label { font-size: 22px; line-height: 20px; text-align: right; }
  .phone { color: var(--tangerine); font-size: 60px; line-height: 64px; letter-spacing: .5px; }
  .email { font-size: 22px; line-height: 28px; letter-spacing: .3px; text-transform: uppercase; }
</style>
</head>
<body>
<div class="canvas">
  <div class="flyer">
    <svg class="flyer-art" width="849" height="1199" viewBox="0 0 849 1199">
      <defs>
        <linearGradient id="hero-tone" x1="0" y1="0" x2="1" y2="0.3">
          <stop offset="0" stop-color="var(--grass-light)"/>
          <stop offset="0.45" stop-color="var(--grass-dark)"/>
          <stop offset="0.7" stop-color="var(--mower-red)"/>
          <stop offset="1" stop-color="#3a3a3a"/>
        </linearGradient>
        <radialGradient id="trim-tone"><stop offset="0" stop-color="#8cc63f"/><stop offset="1" stop-color="#4e8f2c"/></radialGradient>
        <radialGradient id="hedge-tone"><stop offset="0" stop-color="#e8d44a"/><stop offset="1" stop-color="#2f6b22"/></radialGradient>
        <radialGradient id="leaf-tone"><stop offset="0" stop-color="#c98a2a"/><stop offset="1" stop-color="#3d7a2a"/></radialGradient>
      </defs>
      <rect width="849" height="1199" fill="var(--meadow)"/>
      <path role="img" aria-label="Photo of a red lawn mower cutting fresh green grass"
            d="M0,0 H849 V352 C560,362 260,300 0,178 Z" fill="url(#hero-tone)"/>
      <path d="M0,178 C260,300 560,362 849,352 V410 C700,560 380,700 0,820 Z" fill="var(--forest)"/>
      <circle cx="195" cy="810" r="110" fill="var(--ring)"/>
      <circle role="img" aria-label="Photo of a string trimmer edging grass along a sidewalk" cx="195" cy="810" r="94" fill="url(#trim-tone)"/>
      <circle cx="425" cy="730" r="106" fill="var(--ring)"/>
      <circle role="img" aria-label="Photo of hedge shears trimming a green shrub" cx="425" cy="730" r="91" fill="url(#hedge-tone)"/>
      <circle cx="655" cy="605" r="110" fill="var(--ring)"/>
      <circle role="img" aria-label="Photo of autumn leaves being cleared with a leaf blower" cx="655" cy="605" r="94" fill="url(#leaf-tone)"/>
    </svg>

    <div class="brand-plate"><span class="brand-name">Mr Pellowes Yard Works</span></div>

    <p class="offer offer-lawn">Lawn service<br>starting at <span class="price">$40</span>
      <span class="offer-note">(Mowing, edging, leaf blowing)</span></p>
    <p class="offer offer-tree">Tree trimming<br>starting at <span class="price">$125</span></p>

    <section class="services">
      <h2 class="services-title">Other services:</h2>
      <ul class="services-list">
        <li>Mulching</li>
        <li>Shrub trimming</li>
        <li>Aeration</li>
        <li>Flower bed maintenance</li>
        <li>Fall/spring clean up</li>
        <li>Serving New Braunfels</li>
        <li>Surrounding areas</li>
      </ul>
    </section>

    <section class="contact">
      <p class="contact-lead">To set up and estimate</p>
      <div class="contact-call">
        <span class="call-label">Please<br>call:</span>
        <span class="phone">512 555 0143</span>
      </div>
      <p class="email">Or email: mrpellowesyard@example-mail.net</p>
    </section>
  </div>
</div>
</body>
</html>
```